Vorin Co Premium Matcha brand Label

This is a label design project for a luxury tea brand. Feel free to be creative within the guidelines.
Attached to this project is a document called “Private Label Design Requirements” with the design guidelines and template. There is another document called "Vorin Co Packaging Instructions" this has more details necessary to stick to the guidelines in the first document.

I have also attached the certifications to be included as well as different variations of the logo for you to use.

If you have any questions, I am here.

Need extra days to review

Young, active, fun, enjoy the finer things

```html
<!DOCTYPE html>
<html lang="en">
<head>
<meta charset="utf-8">
<title>Vorin Co Premium Matcha Label</title>
<link rel="stylesheet" href="https://fonts.googleapis.com/css2?family=Marcellus&family=Montserrat:wght@500;700&family=Tenor+Sans&display=swap">
<style>
  :root {
    --backdrop: #9a9b9f;
    --ink: #050607;
    --matcha: #4a8f3e;
    --matcha-light: #6fb95f;
    --matcha-pale: #a9d89a;
    --paper: #f4f4f4;
    --paper-shade: #d9d9d9;
    --text-dark: #1a1f1a;
    --text-light: #f2f2f2;
  }
  * { margin: 0; padding: 0; box-sizing: border-box; }
  html, body { width: 1200px; height: 430px; overflow: hidden; }
  body { background: var(--backdrop); font-family: "Montserrat", sans-serif; }
  .label {
    position: absolute; left: 20px; top: 55px;
    width: 1160px; height: 320px;
    box-shadow: 0 6px 18px rgba(0,0,0,0.25);
  }
  .label-art { position: absolute; inset: 0; }
  .panel-back-info {
    position: absolute; left: 36px; top: 128px;
    font-size: 12px; font-weight: 700; line-height: 1.3; color: var(--text-dark);
  }
  .panel-back-info .certified { margin-top: 8px; }
  .brand-lockup {
    position: absolute; left: 412px; top: 112px;
    display: flex; align-items: center; gap: 8px;
  }
  .brand-dot { width: 14px; height: 14px; border-radius: 50%; background: var(--matcha-light); }
  .brand-name { font-family: "Marcellus", serif; font-size: 24px; color: var(--matcha-light); }
  .product-title {
    position: absolute; left: 558px; top: 66px;
    font-family: "Marcellus", serif; color: var(--text-light);
    font-size: 27px; line-height: 1.05;
  }
  .product-title .rule { width: 218px; height: 2px; background: var(--matcha-light); margin: 6px 0 4px; }
  .product-title .product-name {
    font-family: "Tenor Sans", sans-serif; font-size: 42px;
    color: var(--matcha-light); letter-spacing: -1px; line-height: 1;
  }
  .net-weight {
    position: absolute; left: 532px; top: 278px;
    font-family: "Tenor Sans", sans-serif; font-size: 15px; color: var(--text-dark);
  }
  .panel-details {
    position: absolute; left: 846px; top: 92px; width: 270px;
    color: var(--text-dark);
  }
  .panel-details h3 { font-size: 13px; font-weight: 700; }
  .panel-details p, .panel-details li { font-size: 9.5px; font-weight: 700; line-height: 1.3; }
  .panel-details ul { list-style: none; margin-bottom: 8px; }
  .panel-details ul li::before { content: "• "; }
  .panel-details .ingredients { margin-bottom: 6px; }
  .cert-row { display: flex; align-items: center; gap: 8px; }
  .badge-square { width: 22px; height: 22px; background: var(--matcha); }
  .badge-circle { width: 22px; height: 22px; border-radius: 50%; background: var(--matcha); }
  .storage-note { font-size: 9.5px; font-weight: 700; line-height: 1.25; margin-left: 6px; }
</style>
</head>
<body>
  <div class="label">
    <svg class="label-art" viewBox="0 0 1160 320" width="1160" height="320" aria-hidden="true">
      <defs>
        <linearGradient id="greenSide" x1="0" y1="0" x2="1" y2="0">
          <stop offset="0" stop-color="#3f8236"/>
          <stop offset="1" stop-color="#7cc06a"/>
        </linearGradient>
        <linearGradient id="paperSide" x1="0" y1="0" x2="1" y2="1">
          <stop offset="0" stop-color="#f7f7f7"/>
          <stop offset="1" stop-color="#d6d6d6"/>
        </linearGradient>
      </defs>
      <!-- back info panel -->
      <rect class="back-bg" x="0" y="0" width="360" height="320" fill="url(#greenSide)"/>
      <path d="M250,0 H360 V160 C330,100 295,40 250,0 Z" fill="#050607"/>
      <path d="M240,0 C290,45 330,110 360,180" fill="none" stroke="#f4f4f4" stroke-width="4"/>
      <!-- front panel -->
      <rect x="360" y="0" width="440" height="320" fill="#f4f4f4"/>
      <path d="M360,0 H800 V120 C760,225 660,255 570,252 C460,248 385,205 360,150 Z" fill="#050607"/>
      <path d="M360,150 C385,205 460,248 570,252 C660,255 760,225 800,120 V205 C760,290 660,322 570,320 C470,318 395,280 360,235 Z" fill="#4a8f3e"/>
      <path d="M360,165 C390,230 470,268 570,270" fill="none" stroke="#f4f4f4" stroke-width="3"/>
      <path d="M575,252 C665,255 760,222 800,118" fill="none" stroke="#f4f4f4" stroke-width="3"/>
      <!-- details panel -->
      <rect x="800" y="0" width="360" height="320" fill="url(#paperSide)"/>
      <path d="M800,0 H860 L800,110 Z" fill="#050607"/>
      <path d="M860,0 H878 L800,150 V110 Z" fill="#4a8f3e"/>
      <rect x="1118" y="0" width="42" height="320" fill="#a9d89a"/>
    </svg>

    <div class="panel-back-info">
      <p>Product of Japan</p>
      <p>Distributed by:</p>
      <p>Vorin Co | Elmridge, Ga</p>
      <p class="certified">Certified Organic by Verdant Cert</p>
    </div>

    <div class="brand-lockup">
      <span class="brand-dot"></span>
      <span class="brand-name">Vorin Co</span>
    </div>

    <div class="product-title">
      <div>Premium Organic</div>
      <div>Ceremonial</div>
      <div class="rule"></div>
      <div class="product-name">MATCHA</div>
    </div>

    <div class="net-weight">Net Wt: 30g</div>

    <div class="panel-details">
      <h3>Ingredients:</h3>
      <p class="ingredients">Premium Organic Japanese Matcha Green Tea</p>
      <h3>Instructions:</h3>
      <ul>
        <li>2 tsp of Matcha</li>
        <li>2oz of Water (170-180 degrees F)</li>
        <li>Whisk in a W formation until frothy</li>
        <li>Sweeten to taste</li>
      </ul>
      <div class="cert-row">
        <span class="badge-square"></span>
        <span class="badge-circle"></span>
        <p class="storage-note">KEEP REFRIGERATED<br>FOR QUALITY</p>
      </div>
    </div>
  </div>
</body>
</html>
```